Criação de Kit com 6 Layouts de Post para Redes Sociais (Facebook, Instagram e etc) + Capa de Facebook para Marketing & Comunicação
A empresa queria:
" EMPRESA ESPECIALIZADA EM IMPRESSÃO OFFSET E DIGITAL ATENDENDO PEQUENAS MEDIAS E GRANDES TIRAGENS "

```html
<!DOCTYPE html>
<html lang="pt-BR">
<head>
<meta charset="UTF-8">
<title>Impressão Offset — Post</title>
<link rel="stylesheet" href="https://fonts.googleapis.com/css2?family=Roboto:wght@500;700&display=swap">
<style>
  :root {
    --bg-dark: #353535;
    --text-light: #ffffff;
    --accent-teal: #4cc4b8;
    --logo-purple: #9a5cae;
    --photo-pink: #e98fd0;
    --photo-violet: #a98be6;
    --photo-orange: #f2a08a;
    --photo-blue: #7fd0ee;
    --wave-pink: #e97fc8;
    --wave-violet: #8e5fd6;
    --wave-deep: #5b3aa8;
  }
  * { margin: 0; padding: 0; box-sizing: border-box; }
  html, body { width: 1200px; height: 1200px; overflow: hidden; background: var(--bg-dark); }
  .post {
    position: relative;
    width: 1200px;
    height: 1200px;
    background: var(--bg-dark);
    font-family: "Roboto", Arial, sans-serif;
    color: var(--text-light);
    overflow: hidden;
  }
  .post__art { position: absolute; inset: 0; width: 1200px; height: 1200px; }
  .headline {
    position: absolute;
    left: 650px;
    top: 582px;
    font-size: 86px;
    font-weight: 500;
    line-height: 1.08;
    letter-spacing: 2px;
  }
  .rule {
    position: absolute;
    top: 870px;
    width: 68px;
    height: 6px;
    background: var(--accent-teal);
  }
  .rule--left { left: 354px; }
  .rule--right { left: 778px; }
  .brand {
    position: absolute;
    left: 451px;
    top: 797px;
    width: 230px;
    height: 230px;
    border-radius: 50%;
    background: var(--logo-purple);
    display: flex;
    align-items: center;
    justify-content: center;
    font-size: 34px;
    font-weight: 700;
    letter-spacing: 1px;
  }
  .phone {
    position: absolute;
    left: 166px;
    top: 914px;
    font-size: 34px;
    font-weight: 700;
  }
  .tagline {
    position: absolute;
    left: 778px;
    top: 872px;
    font-size: 27px;
    font-weight: 700;
    line-height: 1.2;
  }
</style>
</head>
<body>
<main class="post">
  <svg class="post__art" viewBox="0 0 1200 1200" xmlns="http://www.w3.org/2000/svg">
    <defs>
      <linearGradient id="photoTone" x1="0" y1="0" x2="1" y2="1">
        <stop offset="0" stop-color="var(--photo-violet)"/>
        <stop offset="0.35" stop-color="var(--photo-pink)"/>
        <stop offset="0.6" stop-color="var(--photo-orange)"/>
        <stop offset="1" stop-color="#d46bb8"/>
      </linearGradient>
      <linearGradient id="bubbleTone" x1="0" y1="0" x2="1" y2="1">
        <stop offset="0" stop-color="var(--photo-blue)"/>
        <stop offset="1" stop-color="var(--photo-violet)"/>
      </linearGradient>
      <linearGradient id="wavePink" x1="0" y1="0" x2="1" y2="0">
        <stop offset="0" stop-color="var(--wave-pink)"/>
        <stop offset="1" stop-color="#c77be0"/>
      </linearGradient>
      <linearGradient id="waveViolet" x1="0" y1="0" x2="1" y2="0">
        <stop offset="0" stop-color="var(--wave-violet)"/>
        <stop offset="1" stop-color="var(--wave-pink)"/>
      </linearGradient>
    </defs>

    <path role="img" aria-label="Foto de impressos coloridos em tons de rosa, lilás e laranja"
      fill="url(#photoTone)"
      d="M0 0 H1200 V400 C1200 520 1140 580 1050 570 C930 556 860 440 740 420
         C610 398 520 470 380 455 C240 440 150 410 0 440 Z"/>

    <g role="img" aria-label="Detalhes da foto de impressos em círculos">
      <circle cx="312" cy="564" r="108" fill="url(#bubbleTone)"/>
      <circle cx="523" cy="552" r="38" fill="url(#bubbleTone)"/>
      <circle cx="214" cy="756" r="58" fill="url(#bubbleTone)"/>
    </g>

    <g class="waves">
      <path fill="url(#wavePink)"
        d="M0 1010 C150 970 260 1010 380 1060 C520 1118 640 1050 780 1040
           C930 1030 1060 1080 1200 1040 V1200 H0 Z"/>
      <path fill="url(#waveViolet)"
        d="M0 1090 C160 1060 300 1120 460 1140 C620 1160 760 1090 900 1090
           C1030 1090 1120 1130 1200 1110 V1200 H0 Z"/>
      <path fill="var(--wave-deep)" opacity="0.85"
        d="M0 1160 C200 1140 380 1190 600 1180 C820 1170 1000 1150 1200 1170 V1200 H0 Z"/>
    </g>
  </svg>

  <h1 class="headline">IMPRESSÃO<br>OFFSET</h1>

  <span class="rule rule--left"></span>
  <span class="rule rule--right"></span>

  <div class="brand">LOGO</div>

  <p class="phone">00 00000-0000</p>

  <p class="tagline">Mais de 20 anos<br>imprimindo<br>credibilidade</p>
</main>
</body>
</html>
```